Velno Recycling needs a new web design

We need a new web design for our company based in Austin, TX. We resell and recycling electronics such as laptops, computer components, Tovlets, Brunos, etc. Since our inception over ten years ago, we’ve become one of the premier electronics recycling and remarketing companies in Austin, Texas.

```html
<!DOCTYPE html>
<html lang="en">
<head>
<meta charset="utf-8">
<title>Velno Recycling</title>
<link href="https://fonts.googleapis.com/css2?family=Open+Sans:wght@400;600;700&family=Roboto:wght@400;500;700&display=swap" rel="stylesheet">
<style>
:root{
  --blue:#1a6fc0;
  --blue-dark:#0f5ca8;
  --yellow:#fbc831;
  --yellow-deep:#f6b81c;
  --ink:#333;
  --muted:#555;
  --grey-band:#eeeeee;
  --footer:#04202b;
  --footer-line:#4b6270;
  --white:#fff;
}
*{margin:0;padding:0;box-sizing:border-box}
html,body{width:1200px;height:2436px;overflow:hidden}
body{font-family:"Open Sans",Arial,sans-serif;color:var(--ink);background:var(--white);position:relative}
.wrap{position:absolute;left:133px;width:934px}

/* top bar */
.topbar{position:absolute;top:0;left:0;width:1200px;height:33px;background:var(--blue);color:var(--white);font-size:13px}
.topbar .welcome{position:absolute;left:133px;top:8px;font-weight:600}
.topbar .call{position:absolute;left:648px;top:0;height:33px;width:240px;background:var(--yellow);clip-path:polygon(14px 0,100% 0,100% 100%,0 100%);color:#1d3b5a;padding:8px 0 0 34px}
.topbar .web{position:absolute;left:858px;top:0;height:33px;width:212px;background:var(--blue-dark);clip-path:polygon(20px 0,100% 0,100% 100%,0 50%);padding:8px 0 0 30px}
.topbar svg{position:absolute;top:10px}

/* header */
.header{position:absolute;top:33px;left:0;width:1200px;height:87px;background:var(--white)}
.brand{position:absolute;left:133px;top:20px;display:flex;align-items:center;gap:10px}
.brand .dot{width:48px;height:48px;border-radius:50%;background:var(--blue)}
.brand .name{font-family:"Roboto",sans-serif;font-weight:700;font-size:30px;color:var(--blue);line-height:1}
.nav{position:absolute;right:148px;top:36px;display:flex;gap:40px;font-size:13px;color:#333}
.nav .active{color:var(--blue)}

/* hero */
.hero{position:absolute;top:120px;left:0;width:1200px;height:401px;background:linear-gradient(100deg,#1f4f86 0%,#3a6ea8 45%,#5b8cc0 75%,#4b7cb2 100%)}
.hero-text{position:absolute;left:133px;top:86px;color:var(--white);font-family:"Roboto",sans-serif}
.hero-text .hi{font-size:24px;font-weight:700}
.hero-text h1{font-size:40px;font-weight:700;color:var(--yellow);margin-top:2px;letter-spacing:-0.5px}
.hero-text p{font-family:"Open Sans",sans-serif;font-size:15px;width:560px;margin-top:14px;line-height:1.3}
.hero-btn{position:absolute;left:133px;top:259px;width:139px;height:47px;border:2px solid var(--yellow);border-radius:4px;color:var(--white);font-size:15px;display:flex;align-items:center;justify-content:center}
.arrow-btn{position:absolute;top:164px;width:40px;height:40px;border:2px solid var(--white);border-radius:50%}
.arrow-btn svg{position:absolute;left:11px;top:11px}

/* call band */
.callband{position:absolute;top:521px;left:0;width:1200px;height:120px;background:var(--yellow)}
.callband .lead{position:absolute;left:133px;top:25px;width:290px;font-size:12.5px;font-weight:600;color:var(--blue-dark);line-height:1.65}
.callband .sep{position:absolute;top:16px;width:1px;height:88px;background:#d8a21c}
.callband .phone{position:absolute;left:468px;top:30px}
.callband .toll{position:absolute;left:535px;top:26px;color:#1d1d1d;font-family:"Roboto",sans-serif}
.callband .toll .t{font-size:21px}
.callband .toll .n{font-size:27px;font-weight:700;margin-top:-3px}
.callband .callnow{position:absolute;left:895px;top:36px;width:171px;height:48px;border-radius:24px;background:var(--blue);color:var(--white);font-size:16px;font-weight:600;display:flex;align-items:center;justify-content:center;gap:8px}

/* section headings */
.sec-title{position:absolute;left:0;width:1200px;text-align:center}
.sec-title h2{font-size:28px;font-weight:700;color:#4a4a4a;letter-spacing:-0.3px}
.sec-title .rule{display:block;margin:6px auto 0}
.sec-title p{font-size:13px;color:#333;margin-top:16px;line-height:1.6}

/* services */
.card{position:absolute;top:861px;width:257px;height:238px;border:1px solid #e6e6e6;background:var(--white)}
.card .icon{position:absolute;left:-31px;top:-23px;width:62px;height:62px;border-radius:50%;border:2px solid var(--blue);background:var(--white);display:flex;align-items:center;justify-content:center}
.card h3{position:absolute;left:22px;top:32px;width:220px;font-size:17px;font-weight:600;color:var(--blue);line-height:1.2}
.card p{position:absolute;left:22px;top:84px;width:220px;font-size:12.5px;color:#555;line-height:1.6;text-align:justify}
.card .more{position:absolute;left:29px;top:183px;width:106px;height:32px;border:1px solid #555;font-size:12.5px;color:#333;display:flex;align-items:center;justify-content:center}

/* about */
.about{position:absolute;top:1159px;left:0;width:1200px;height:405px;background:var(--grey-band)}
.about .kicker{position:absolute;left:133px;top:49px;font-size:13px;font-weight:600;color:#222}
.about h2{position:absolute;left:133px;top:70px;font-size:28px;font-weight:600;color:var(--blue);letter-spacing:-0.3px}
.about .bio{position:absolute;left:133px;top:138px;width:510px;font-size:13.5px;line-height:1.55;color:#333;text-align:justify}
.about .who{position:absolute;left:133px;top:300px;font-size:15px;font-weight:700;color:#111}
.about .role{position:absolute;left:133px;top:322px;font-size:12.5px;color:#444}
.about .photo{position:absolute;left:685px;top:52px;width:382px;height:283px;background:var(--white);padding:7px}
.about .photo div{width:100%;height:100%;background:linear-gradient(120deg,#dfe7ec 0%,#b9c9d3 45%,#3c4652 70%,#c9d4dc 100%)}

/* policies */
.policy{position:absolute;top:1744px;width:296px;height:186px;padding:6px}
.policy .inner{width:100%;height:100%;border:1px solid rgba(255,255,255,.85);display:flex;align-items:center;justify-content:center;text-align:center;color:var(--white);font-size:13.5px;font-weight:600;text-transform:uppercase;line-height:1.6;padding:0 20px}
.policy.blue{background:var(--blue)}
.policy.yellow{background:var(--yellow)}

/* footer */
.footer{position:absolute;top:1998px;left:0;width:1200px;height:438px;background:var(--footer);color:var(--white)}
.footer h4{position:absolute;top:45px;font-size:15px;font-weight:400;letter-spacing:.5px}
.footer .bar{position:absolute;top:77px;width:27px;height:3px;background:var(--white)}
.footer .about-txt{position:absolute;left:133px;top:96px;width:300px;font-size:11.5px;line-height:1.6;text-align:justify}
.footer .links{position:absolute;top:98px;font-size:12px;list-style:none}
.footer .links li{margin-bottom:14px;display:flex;align-items:center;gap:12px}
.infobox{position:absolute;top:2210px;height:98px;width:190px;border:1px solid var(--footer-line);text-align:center;font-size:11.5px;color:#cfd6da;line-height:1.45;padding-top:12px}
.infobox svg{display:block;margin:0 auto 10px}
.field{position:absolute;left:804px;width:263px;height:36px;background:var(--white);color:#444;font-size:13px;padding:8px 16px}
.submit{position:absolute;left:807px;top:2269px;width:104px;height:39px;background:var(--yellow-deep);color:var(--white);font-size:13.5px;font-weight:600;letter-spacing:1px;display:flex;align-items:center;justify-content:center}
.footer .bottom{position:absolute;top:365px;left:0;width:1200px;height:1px;background:#13323e}
.footer .copy{position:absolute;left:133px;top:391px;font-size:12px}
.footer .social{position:absolute;left:975px;top:391px;display:flex;gap:10px}
.footer .social span{width:14px;height:14px;border-radius:50%;background:var(--white)}
</style>
</head>
<body>

<div class="topbar">
  <span class="welcome">Welcome to our website Velno Recycling</span>
  <div class="call">
    <svg width="12" height="12" viewBox="0 0 24 24" style="left:20px"><path fill="#1d3b5a" d="M6.6 10.8a15 15 0 0 0 6.6 6.6l2.2-2.2c.3-.3.7-.4 1-.2 1.1.4 2.3.6 3.6.6.6 0 1 .4 1 1V20c0 .6-.4 1-1 1A17 17 0 0 1 3 4c0-.6.4-1 1-1h3.5c.6 0 1 .4 1 1 0 1.3.2 2.5.6 3.6.1.3 0 .7-.2 1z"/></svg>
    Call + (512)555-0147
  </div>
  <div class="web">
    <svg width="12" height="12" viewBox="0 0 24 24" style="left:12px"><circle cx="12" cy="12" r="10" fill="#fff"/></svg>
    www.velnorecycling.com
  </div>
</div>

<header class="header">
  <div class="brand"><span class="dot"></span><span class="name">Velno Recycling</span></div>
  <nav class="nav">
    <span class="active">HOME</span><span>ABOUT US</span><span>SERVICES</span><span>OUR POLICIES</span><span>CONTACT US</span>
  </nav>
</header>

<section class="hero" role="img" aria-label="Blue-tinted photo of a hand holding a stylus over a circuit board pattern">
  <div class="hero-text">
    <div class="hi">Welcome to</div>
    <h1>Velno Recycling Services</h1>
    <p>What most people do not realize is electronic waste represents 2% of America's trash in landfills, but it equals 70% of overall toxic waste.</p>
  </div>
  <div class="hero-btn">Contact Us</div>
  <div class="arrow-btn" style="left:20px"><svg width="14" height="14" viewBox="0 0 14 14"><path d="M9 2 4 7l5 5" stroke="#fff" stroke-width="2" fill="none"/></svg></div>
  <div class="arrow-btn" style="left:1140px"><svg width="14" height="14" viewBox="0 0 14 14"><path d="M5 2l5 5-5 5" stroke="#fff" stroke-width="2" fill="none"/></svg></div>
</section>

<section class="callband">
  <p class="lead">That is one of the reasons we started Velno Recycling in 2006 to fill the void as a full service computer and electronic waste recycling "one stop shop."</p>
  <span class="sep" style="left:440px"></span>
  <svg class="phone" width="56" height="60" viewBox="0 0 24 24"><path fill="#1d1d1d" d="M6.6 10.8a15 15 0 0 0 6.6 6.6l2.2-2.2c.3-.3.7-.4 1-.2 1.1.4 2.3.6 3.6.6.6 0 1 .4 1 1V20c0 .6-.4 1-1 1A17 17 0 0 1 3 4c0-.6.4-1 1-1h3.5c.6 0 1 .4 1 1 0 1.3.2 2.5.6 3.6.1.3 0 .7-.2 1z"/><path d="M14 2.5a8 8 0 0 1 7.5 7.5M14 6a4.5 4.5 0 0 1 4 4" stroke="#1d1d1d" stroke-width="1.6" fill="none"/></svg>
  <div class="toll"><div class="t">Get Toll Free Number</div><div class="n">(844)55-VELNO (83566)</div></div>
  <span class="sep" style="left:840px"></span>
  <div class="callnow">Call Us Now <svg width="14" height="14" viewBox="0 0 14 14"><circle cx="7" cy="7" r="7" fill="var(--yellow)"/><path d="M4 7h6M7.5 4.5 10 7l-2.5 2.5" stroke="#1a6fc0" stroke-width="1.6" fill="none"/></svg></div>
</section>

<section class="sec-title" style="top:680px">
  <h2>OUR SERVICES</h2>
  <svg class="rule" width="116" height="10" viewBox="0 0 116 10"><path d="M0 5h52M64 5h52" stroke="#1a6fc0"/><circle cx="58" cy="5" r="4" fill="none" stroke="#1a6fc0"/></svg>
  <p>From Data Destruction with our state of the art Degaussing equipment to our Cloud Based CRM Product Inventory system, Velno<br>Recycling proves that we care about keeping our clients recycle and remarketing equipment safe and secure.</p>
</section>

<article class="card" style="left:162px">
  <div class="icon"><svg width="26" height="24" viewBox="0 0 26 24"><rect x="1" y="2" width="24" height="15" rx="1" fill="#1a6fc0"/><rect x="3" y="4" width="20" height="11" fill="#fff"/><rect x="10" y="18" width="6" height="3" fill="#1a6fc0"/><rect x="7" y="21" width="12" height="2" fill="#1a6fc0"/></svg></div>
  <h3>Computer and electronic Waste recycling</h3>
  <p>"one stop shop." Since our inception over ten years ago, we've become one of the premier electronics recycling and remarketing our customers....</p>
  <div class="more">READ MORE</div>
</article>
<article class="card" style="left:487px">
  <div class="icon"><svg width="24" height="24" viewBox="0 0 24 24"><path d="M12 3l4 6h-8zM4 19l3-7 4 6zM20 19l-7-1 4-6z" fill="#1a6fc0"/></svg></div>
  <h3>Approach To every Recycling job</h3>
  <p>We have gained a large market share of the electronic waste recycling and electronics marketing business within Texas and throughout the county.</p>
  <div class="more">READ MORE</div>
</article>
<article class="card" style="left:812px">
  <div class="icon"><svg width="26" height="18" viewBox="0 0 26 18"><path d="M6 17a5 5 0 0 1 0-10 7 7 0 0 1 13-1 5.5 5.5 0 0 1 1 11z" fill="#1a6fc0"/></svg></div>
  <h3>Cloud Based CRM Product Inventory system</h3>
  <p>From Data Destruction with our state of the art Degaussing equipment to our Cloud Based CRM Product Inventory equipment ....</p>
  <div class="more">READ MORE</div>
</article>

<section class="about">
  <div class="kicker">CEO of Velno Recycling</div>
  <h2>About Velno Recycling</h2>
  <p class="bio">Dale Ferren is responsible for running all facets of the business. Dale has a proven executive management track record and over 20 years of experience driving sales growth in the Recycling industry. Prior to founding Velno Recycling in 2006, Dale was the Director of Sales for Coastline Electronics Trading Inc. and responsible for all global sales and marketing activities. At CET he led the paradigm shifting transformation into an enterprise-focused company while growing sales 50% year over year.</p>
  <div class="who">Dale Ferren</div>
  <div class="role">CEO of Velno Recycling</div>
  <div class="photo"><div role="img" aria-label="Photo of the company CEO in a suit holding a laptop in a bright office"></div></div>
</section>

<section class="sec-title" style="top:1610px">
  <h2>OUR POLICIES</h2>
  <svg class="rule" width="116" height="10" viewBox="0 0 116 10"><path d="M0 5h52M64 5h52" stroke="#1a6fc0"/><circle cx="58" cy="5" r="4" fill="none" stroke="#1a6fc0"/></svg>
  <p>A few of these policies include the following</p>
</section>

<div class="policy blue" style="left:132px"><div class="inner">To achieve a "Zero Landfill Policy" through the effective management of safety, health, environment and community issues at our facility and with our vendors.</div></div>
<div class="policy yellow" style="left:452px"><div class="inner">It is our belief that all employees, contractors and visitors must feel safe and finish their daily activities without injury or damage to the environment.</div></div>
<div class="policy blue" style="left:771px"><div class="inner">It is our goal to shape employee behavior to recognize risk and prevent harm.</div></div>

<footer class="footer">
  <h4 style="left:133px">ABOUT US</h4><span class="bar" style="left:133px"></span>
  <p class="about-txt">What most people do not realize is electronic waste represents 2% of America's trash in landfills, but it equals 70% of overall toxic waste. Used computer equipment is a rapidly growing source of waste across the country.</p>

  <h4 style="left:502px">INFORMATION LINKS</h4><span class="bar" style="left:502px"></span>
  <ul class="links" style="left:506px">
    <li><svg width="10" height="10" viewBox="0 0 10 10"><path d="M0 5h8M5 2l3 3-3 3" stroke="#fff" stroke-width="1.5" fill="none"/></svg>Home</li>
    <li><svg width="10" height="10" viewBox="0 0 10 10"><path d="M0 5h8M5 2l3 3-3 3" stroke="#fff" stroke-width="1.5" fill="none"/></svg>About Us</li>
    <li><svg width="10" height="10" viewBox="0 0 10 10"><path d="M0 5h8M5 2l3 3-3 3" stroke="#fff" stroke-width="1.5" fill="none"/></svg>Services</li>
  </ul>
  <ul class="links" style="left:650px;top:96px">
    <li><svg width="10" height="10" viewBox="0 0 10 10"><path d="M0 5h8M5 2l3 3-3 3" stroke="#fff" stroke-width="1.5" fill="none"/></svg>Our Policies</li>
    <li><svg width="10" height="10" viewBox="0 0 10 10"><path d="M0 5h8M5 2l3 3-3 3" stroke="#fff" stroke-width="1.5" fill="none"/></svg>Contact Us</li>
  </ul>

  <h4 style="left:804px">CONTACT INFO</h4><span class="bar" style="left:808px"></span>

  <div class="bottom"></div>
  <div class="copy">© 2018 Velno Recycling All Rights Reserved.</div>
  <div class="social"><span></span><span></span><span></span><span></span></div>
</footer>

<div class="infobox" style="left:133px">
  <svg width="16" height="22" viewBox="0 0 16 22"><path d="M8 0a8 8 0 0 0-8 8c0 6 8 14 8 14s8-8 8-14a8 8 0 0 0-8-8zm0 11a3 3 0 1 1 0-6 3 3 0 0 1 0 6z" fill="#cfd6da"/></svg>
  4120 Larkmoor Blvd.<br>Austin, Texas 78757
</div>
<div class="infobox" style="left:336px">
  <svg width="24" height="18" viewBox="0 0 24 18"><rect width="24" height="18" rx="1" fill="#cfd6da"/><path d="M1 1l11 9 11-9" stroke="#04202b" stroke-width="1.6" fill="none"/></svg>
  Dale@VelnoRecycling.com<br>www.VelnoRecycling.com
</div>
<div class="infobox" style="left:539px">
  <svg width="18" height="18" viewBox="0 0 24 24"><path fill="#cfd6da" d="M6.6 10.8a15 15 0 0 0 6.6 6.6l2.2-2.2c.3-.3.7-.4 1-.2 1.1.4 2.3.6 3.6.6.6 0 1 .4 1 1V20c0 .6-.4 1-1 1A17 17 0 0 1 3 4c0-.6.4-1 1-1h3.5c.6 0 1 .4 1 1 0 1.3.2 2.5.6 3.6.1.3 0 .7-.2 1z"/></svg>
  Cell : (512)555-0147<br>Fax : (512)555-0192<br>Toll Free : (844)55-VELNO (83566)
</div>

<div class="field" style="top:2097px">Your Name</div>
<div class="field" style="top:2146px">Your Mail</div>
<div class="field" style="top:2195px;height:59px">Message</div>
<div class="submit">SUBMIT</div>

</body>
</html>
```